Microblading website contest - Make it colorful

Beauty salon focusing on microblading need a better website template. Please make a 1 page site mobile optimized and nicer layout with better color formulation. Would love interactive images in the site. You can use stock images and if approve we can pay for it.
Current site:
tessawynkelpeony.com

Inspiration:
https://framqueue.net/shots/41877260-Microblading-HomePage
https://framqueue.net/shots/7914026-Lunetto-Microblading-Eyebrow-Beauty-Salon-Pagewright-Theme

Target Market(s)

women

Industry/Entity Type

beauty salon

Number of Pages Required

1 page

Font styles to use
Serif
Decorative
Script

Requirements
Nice to have
• As pretty as possible

```html
<!DOCTYPE html>
<html lang="en">
<head>
<meta charset="UTF-8">
<title>Microblading – Atelier Brows Tessa</title>
<link href="https://fonts.googleapis.com/css2?family=Lora:wght@400;500;600&family=Montserrat:wght@400;500;600&family=Dancing+Script:wght@400&display=swap" rel="stylesheet">
<style>
:root{
  --pink:#f7a9a8;
  --pink-soft:#fde9e9;
  --pink-blob:#fcdcdc;
  --rose-text:#f2a6a6;
  --script:#c77b78;
  --ink:#1d1d1d;
  --muted:#333;
  --hero-bg:#e9ecf0;
  --gold-wash:rgba(214,180,110,.16);
  --white:#fff;
}
*{margin:0;padding:0;box-sizing:border-box}
html,body{width:1200px;height:4441px;overflow:hidden;background:var(--white)}
body{position:relative;font-family:"Montserrat",sans-serif;color:var(--ink)}
.abs{position:absolute}
.script{font-family:"Dancing Script",cursive;color:var(--script)}
a{color:inherit;text-decoration:none}

/* nav */
.nav{top:0;left:0;width:1200px;height:71px;background:var(--white);display:flex;align-items:center;justify-content:center;font-size:10px}
.nav ul{display:flex;list-style:none;gap:44px}
.nav .brand{font-family:"Lora",serif;font-size:26px;margin:0 22px 4px}
.nav .right{gap:22px}
.cart{margin-left:24px;width:12px;height:10px;background:var(--ink);border-radius:1px 1px 3px 3px}

/* hero */
.hero{top:71px;left:0;width:1200px;height:493px;background:var(--hero-bg)}
.hero-photo{left:0;top:0;width:600px;height:493px;background:linear-gradient(90deg,#e6bda6,#efd6c8 70%,rgba(233,236,240,0))}
.brow-art{top:130px;width:180px;height:26px;background:linear-gradient(90deg,rgba(160,160,165,.15),rgba(140,140,145,.6))}
.hero h1{left:560px;top:190px;font-family:"Lora",serif;font-weight:400;font-size:44px;letter-spacing:1.5px;white-space:nowrap}
.hero .tag{left:559px;top:255px;font-family:"Lora",serif;font-size:30px;color:var(--rose-text);white-space:nowrap}
.btn-line{left:557px;top:313px;width:160px;height:45px;border:1px solid var(--pink);font-family:"Lora",serif;font-size:15px;display:flex;align-items:center;justify-content:center}

/* decorative ornament areas: flat soft wash only */
.ornament-area{background:linear-gradient(135deg,var(--gold-wash),rgba(214,180,110,0))}
.pill{background:var(--pink);border-radius:24px;font-family:"Lora",serif;font-size:15px;display:flex;align-items:center;justify-content:center}

/* about */
.about-title{left:143px;top:706px;font-family:"Lora",serif;font-size:45px;font-weight:400}
.about-text{left:143px;top:785px;width:410px;font-size:11.5px;line-height:21.5px;color:var(--muted)}
.about-text p+p{margin-top:10px;font-weight:500;color:var(--ink)}
.about-blob{left:574px;top:615px;width:486px;height:488px;background:var(--pink-blob);border-radius:52% 48% 40% 60% / 55% 50% 50% 45%}
.about-photo{left:607px;top:615px;width:453px;height:488px;background:linear-gradient(160deg,#8a8a8a,#d9c4b7 45%,#f5f2ef);border-radius:48% 52% 45% 55% / 50% 45% 55% 50%}

/* care band */
.care{top:1229px;left:0;width:1200px;height:519px;background:linear-gradient(180deg,#fde6e6,#fdeeee)}
.care-eye{left:0;top:0;width:180px;height:170px;background:radial-gradient(ellipse at 40% 50%,rgba(200,180,180,.3),rgba(253,230,230,0) 70%)}
.care .kicker{left:0;width:1200px;top:80px;text-align:center;font-size:21px}
.care h2{left:0;width:1200px;top:118px;text-align:center;font-family:"Lora",serif;font-weight:400;font-size:44px}
.feature{top:205px;width:300px;text-align:center}
.feature svg{display:block;margin:0 auto 16px}
.feature h3{font-family:"Lora",serif;font-weight:600;font-size:17px;margin-bottom:10px}
.feature p{font-size:11px;line-height:22px;color:var(--muted)}

/* services */
.section-title{left:0;width:1200px;text-align:center;font-family:"Lora",serif;font-weight:400;font-size:45px}
.section-sub{left:0;width:1200px;text-align:center;font-size:11px;line-height:24px;color:var(--muted)}
.svc-bg{background:var(--pink-soft);border-radius:50% 50% 45% 55% / 55% 45% 55% 45%}
.svc-photo{border-radius:55% 45% 50% 50% / 45% 55% 45% 55%}
.svc h3{font-family:"Lora",serif;font-weight:600;font-size:27px;line-height:34px}
.svc p{font-size:13.5px;line-height:26px;color:var(--muted)}
.svc .note{font-family:"Dancing Script",cursive;color:var(--script);font-size:17px;margin-top:4px}

/* testimonials */
.card{width:287px;background:var(--white);border-radius:38px;box-shadow:0 6px 22px rgba(240,160,160,.18);border:1px solid #fbe4e4;padding:38px 26px 0;text-align:center;font-size:11.5px;line-height:20.5px;color:var(--muted)}
.card.featured{background:var(--pink);color:var(--ink);font-weight:500;border:none}
.card .who{display:flex;align-items:center;gap:10px;border-top:1px solid #ddd;margin-top:18px;padding:14px 0;font-size:12px;font-weight:600;text-align:left}
.card.featured .who{border-top-color:#7aa9d8;color:var(--white)}
.card .init{width:30px;height:30px;border-radius:50%;border:1.5px solid var(--ink);display:flex;align-items:center;justify-content:center;font-size:11px;background:var(--white);color:var(--ink)}
.card .stars{margin-left:auto;color:#f4a340;letter-spacing:2px;font-size:12px}
.card.featured .stars{color:var(--white)}
.quote{position:absolute;left:18px;top:12px;font-family:"Lora",serif;font-size:80px;color:#f3f3f3;line-height:1}
.arrow{width:27px;height:27px;border-radius:50%;display:flex;align-items:center;justify-content:center}

/* gallery */
.gallery-band{top:3689px;left:0;width:1200px;height:466px;background:linear-gradient(100deg,#dfe7f7,#f7e3ef 30%,#eef5e6 60%,#f8f1d4 85%,#f7e4ef)}
.gallery-band h2{left:0;width:1200px;top:90px;text-align:center;font-family:"Lora",serif;font-weight:400;font-size:45px}
.shot{top:156px;width:224px;height:222px}

/* footer */
.foot h4{font-family:"Lora",serif;font-weight:600;font-size:17px}
.foot-links{display:grid;grid-template-columns:104px 140px;row-gap:22px;font-size:11px}
.social{display:flex;gap:14px}
.social span{width:26px;height:26px;border-radius:50%;background:var(--pink)}
.contact-row{display:flex;gap:14px;align-items:flex-start;font-size:10px;line-height:16px;margin-bottom:14px}
.contact-row .ic{width:30px;height:30px;border-radius:50%;background:var(--pink-soft);display:flex;align-items:center;justify-content:center;flex:none}
.copy{left:0;top:4396px;width:1200px;height:45px;background:var(--pink);display:flex;align-items:center;justify-content:center;font-size:11px}
</style>
</head>
<body>

<header class="abs nav">
  <ul><li>Home</li><li>About</li><li>Services</li><li>Gallery</li><li>Shop</li></ul>
  <span class="brand">Microblading</span>
  <ul class="right"><li>Academy</li><li>Contact Us</li><li>Customer Feedback</li><li>More ▾</li></ul>
  <span class="cart" role="img" aria-label="Cart"></span>
</header>

<section class="abs hero">
  <div class="abs hero-photo" role="img" aria-label="Close-up portrait of a woman with groomed eyebrows"></div>
  <div class="abs brow-art" style="left:570px" role="img" aria-label="Sketched left eyebrow"></div>
  <div class="abs brow-art" style="left:790px;transform:scaleX(-1)" role="img" aria-label="Sketched right eyebrow"></div>
  <h1 class="abs">ATELIER BROWS TESSA</h1>
  <div class="abs tag">Your Personal Eyebrow Specialist</div>
  <a class="abs btn-line">Contact Us</a>
</section>

<!-- about -->
<div class="abs ornament-area" style="left:18px;top:590px;width:285px;height:170px" role="img" aria-label="Golden leaf branch ornament"></div>
<h2 class="abs about-title">About Tessa</h2>
<div class="abs about-text">
  <p>Tessa has 7 years of microblading experience. She graduated from NovaLine United States. After, she studied in Arcline Academy, a global top brand from Germany. She was personally guided by the brand CEO Marek Dolan and the first China Master Wen Liu.</p>
  <p>After earning award of ArcBrows Artist in 2019. Tessa continued her practice microblading until she won the world's first ArcBrows Master in Taiwan in 2021. She is currently the only certificated Master technician in Taiwan. She also holds a shading and ArcGlow Master.</p>
</div>
<a class="abs pill" style="left:141px;top:990px;width:161px;height:44px">Learn More</a>
<div class="abs about-blob"></div>
<div class="abs about-photo" role="img" aria-label="Portrait of the brow specialist in a white top"></div>
<div class="abs ornament-area" style="left:925px;top:880px;width:265px;height:280px" role="img" aria-label="Golden leaf branch ornament"></div>

<!-- care band -->
<section class="abs care">
  <div class="abs care-eye" role="img" aria-label="Faint sketch of an eye with lashes"></div>
  <div class="abs kicker script">Let us take care of</div>
  <h2 class="abs">Your Eyebrows and Beauty</h2>
  <div class="abs feature" style="left:131px">
    <svg width="52" height="36" viewBox="0 0 52 36" fill="none" stroke="#c77b78" stroke-width="1.6"><path d="M3 20c8-10 20-14 30-10s14 10 16 10c-6 6-14 10-24 10S8 26 3 20z"/><circle cx="25" cy="20" r="6"/></svg>
    <h3>Licensed Microblading Artist</h3>
    <p>License from various states in<br>United State</p>
  </div>
  <div class="abs feature" style="left:450px">
    <svg width="40" height="40" viewBox="0 0 40 40" fill="none" stroke="#c77b78" stroke-width="1.6"><circle cx="20" cy="20" r="17"/><path d="M12 20l6 6 10-12"/></svg>
    <h3>Years of Experience</h3>
    <p>Over thousands of cases<br>Oversea study and practice</p>
  </div>
  <div class="abs feature" style="left:767px">
    <svg width="44" height="44" viewBox="0 0 44 44" fill="none" stroke="#c77b78" stroke-width="1.6"><circle cx="22" cy="22" r="19"/><circle cx="22" cy="22" r="12"/></svg>
    <h3>European Latest Technique</h3>
    <p>We study European-style natural<br>hair flow, improve and make it<br>suitable for Asians</p>
  </div>
  <a class="abs pill" style="left:521px;top:388px;width:158px;height:43px">Show More</a>
</section>

<!-- services -->
<div class="abs ornament-area" style="left:915px;top:1752px;width:260px;height:180px" role="img" aria-label="Golden leaf branch ornament"></div>
<h2 class="abs section-title" style="top:1822px">Specialized Services</h2>
<div class="abs section-sub" style="top:1892px">We treat every client as our friends and family. We give you the most sincere advise and best quality and service.<br>We do not only follow the trend. We hear you, and want you to love it forever.</div>

<div class="abs svc-bg" style="left:200px;top:1965px;width:300px;height:340px"></div>
<div class="abs svc-photo" style="left:147px;top:1978px;width:340px;height:337px;background:linear-gradient(140deg,#7a6c68,#e8d2c6 50%,#f3ece8)" role="img" aria-label="Technician microblading a client's eyebrow"></div>
<div class="abs svc" style="left:646px;top:2093px">
  <h3>Natural Brows</h3>
  <p>Microblading | Hand-drawing hair lines</p>
  <div class="note">For all skin type</div>
</div>

<div class="abs ornament-area" style="left:0;top:2275px;width:185px;height:170px" role="img" aria-label="Golden leaf branch ornament"></div>
<div class="abs svc" style="left:143px;top:2418px;width:400px">
  <h3>Powder Eyeliner<br>(Natural Eyeshadow)</h3>
  <p style="margin-top:6px">Extend eyeline at end of the eye| With a touch of ligh<br>eyeshadow vision</p>
  <p style="margin-top:4px">For those who like to have an eye makeup filter</p>
  <div class="note">24/7 | Eye-shape adjustment</div>
</div>
<div class="abs svc-bg" style="left:643px;top:2360px;width:300px;height:335px"></div>
<div class="abs svc-photo" style="left:660px;top:2340px;width:331px;height:355px;background:linear-gradient(160deg,#8c8f94,#d8b9a8 50%,#9fb6cf)" role="img" aria-label="Woman with defined eyeliner touching her face"></div>

<div class="abs svc-bg" style="left:147px;top:2705px;width:345px;height:330px"></div>
<div class="abs svc-photo" style="left:147px;top:2698px;width:335px;height:340px;background:linear-gradient(150deg,#f0f0f0,#d9c2b6 45%,#3a3030 85%)" role="img" aria-label="Scalp micropigmentation treatment on a client"></div>
<div class="abs svc" style="left:646px;top:2787px;width:400px">
  <h3>Scalp Micropigmentation</h3>
  <p style="margin-top:4px">Add destiny to the thinning area| &nbsp; Seamless and Undetectable| &nbsp; Accommodates your skin tone and natural hair color | providing the appearance of hair</p>
  <div class="note">For restoring hairline | Bald spots | Scar covering</div>
</div>
<a class="abs pill" style="left:521px;top:3072px;width:158px;height:45px">Services</a>

<!-- testimonials -->
<div class="abs ornament-area" style="left:10px;top:3195px;width:145px;height:235px" role="img" aria-label="Golden leaf outline ornament"></div>
<div class="abs script" style="left:0;width:1200px;top:3200px;text-align:center;font-size:21px">Testimonials</div>
<h2 class="abs section-title" style="top:3237px">What Peoples Say</h2>

<div class="abs card" style="left:141px;top:3355px"><span class="quote">“</span>
  Lorem ipsum dolor sit amet, consectetuer adipiscing elit, sed diam non ummy nibh euismod tincidunt ut laoreet dolore magna aliquam erat vo lutpat. Ut wisi enim ad minim veniam.
  <div class="who"><span class="init">MH</span>Maya Hollis<span class="stars">★★★★★</span></div>
</div>
<div class="abs card featured" style="left:455px;top:3317px">
  Lorem ipsum dolor sit amet, consectetuer adipiscing elit, sed diam non ummy nibh euismod tincidunt ut laoreet dolore magna aliquam erat vo lutpat. Ut wisi enim ad minim veniam.
  <div class="who"><span class="init">CB</span>Clara Benn<span class="stars">★★★★★</span></div>
</div>
<div class="abs card" style="left:771px;top:3355px"><span class="quote">“</span>
  Lorem ipsum dolor sit amet, consectetuer adipiscing elit, sed diam non ummy nibh euismod tincidunt ut laoreet dolore magna aliquam erat vo lutpat. Ut wisi enim ad minim veniam.
  <div class="who"><span class="init">JP</span>June Porter<span class="stars">★★★★★</span></div>
</div>
<div class="abs arrow" style="left:568px;top:3574px;border:1.5px solid var(--ink)"><svg width="10" height="10" viewBox="0 0 10 10"><path d="M7 1L3 5l4 4" stroke="#1d1d1d" stroke-width="1.8" fill="none"/></svg></div>
<div class="abs arrow" style="left:603px;top:3574px;background:var(--pink)"><svg width="10" height="10" viewBox="0 0 10 10"><path d="M3 1l4 4-4 4" stroke="#fff" stroke-width="1.8" fill="none"/></svg></div>

<!-- gallery -->
<section class="abs gallery-band">
  <h2 class="abs">#Lookbook</h2>
  <div class="abs shot" style="left:141px;background:linear-gradient(160deg,#3b3b3b,#d8c9c0 60%,#e8e2de)" role="img" aria-label="Artists working on a client in the studio"></div>
  <div class="abs shot" style="left:372px;background:linear-gradient(160deg,#f1f1f1,#cfc7c2 60%,#7b7776)" role="img" aria-label="Training session in a bright classroom"></div>
  <div class="abs shot" style="left:603px;background:linear-gradient(160deg,#ececec,#b8aca6 55%,#2d2b2b)" role="img" aria-label="Graduates holding certificates"></div>
  <div class="abs shot" style="left:834px;background:linear-gradient(160deg,#e8e4e2,#8f8a8a 55%,#1f1f23)" role="img" aria-label="Artist performing a brow treatment"></div>
</section>

<!-- footer -->
<div class="abs foot" style="left:143px;top:4200px">
  <h4>Quick Links</h4>
  <div class="foot-links" style="margin-top:22px">
    <span>Home</span><span>Shop</span><span>About</span><span>Academy</span><span>Services</span><span>Contact Us</span><span>Gallery</span><span>Customer Feedback</span>
  </div>
</div>
<div class="abs foot" style="left:460px;top:4235px;width:280px;text-align:center">
  <div style="font-family:'Lora',serif;font-size:28px">Microblading</div>
  <div class="social" style="justify-content:center;margin-top:18px"><span></span><span></span><span></span><span></span></div>
</div>
<div class="abs foot" style="left:858px;top:4200px;width:230px">
  <h4>Contact Details</h4>
  <div style="margin-top:22px">
    <div class="contact-row"><span class="ic"><svg width="12" height="14" viewBox="0 0 12 14"><path d="M6 13S1 8 1 5a5 5 0 0110 0c0 3-5 8-5 8z" fill="#c0392b"/><circle cx="6" cy="5" r="1.8" fill="#fde9e9"/></svg></span><span>48-07 Linden Row, Fairhill<br>NY 10482</span></div>
    <div class="contact-row"><span class="ic"><svg width="13" height="13" viewBox="0 0 24 24"><path d="M6.6 10.8a15 15 0 006.6 6.6l2.2-2.2c.3-.3.7-.4 1-.2 1.1.4 2.3.6 3.6.6.6 0 1 .4 1 1V20c0 .6-.4 1-1 1A17 17 0 013 4c0-.6.4-1 1-1h3.5c.6 0 1 .4 1 1 0 1.3.2 2.5.6 3.6.1.3 0 .7-.2 1z" fill="#1d1d1d"/></svg></span><span>Phone<br>555-014-2271</span></div>
    <div class="contact-row"><span class="ic"><svg width="13" height="11" viewBox="0 0 13 11"><rect x="0.5" y="0.5" width="12" height="10" rx="1.5" fill="#1d1d1d"/><path d="M1 1.5l5.5 4.5L12 1.5" stroke="#fde9e9" stroke-width="1.2" fill="none"/></svg></span><span><b>Email</b><br>tessaatelierbrows@mailbox.net</span></div>
  </div>
</div>
<div class="abs copy">© 2023 Atelier Brows Tessa Inc. All Rights Reserved.</div>

</body>
</html>
```